"Drink Champagne and Dance on the Table" sort of business card needed!

We throw events, weddings, engagement parties, baby showers and the sort of end of year corporate events that people remember long after the glitter has settled - the sort of events that make you stand still and say wow when you walk in and then make you want to "Drink Champagne and Dance on the Tables"

We have a great logo with heaps of potential and need a business card that just screams creative professionals!

We are based in Auckland, NZ and are priced at the Premium end of the market were there are around 10 other main competitors. We need to stand out and make a strong statement about who we are!

Our Business Card will be one of the few items that we print out so are fully prepared to invest in a premium print job.

We really love our logo and think it has heaps of potential! Its ok if you would like to manipulate it (maybe put it on an angle, or use the circle element on its own?).

Black and Gold is very striking, but its very done in our market so we would like to avoid a solid black background please

We have done a bit of an inspiration document to give you an idea of the sort of look and feel we are hoping to achieve.

Target Market(s)

Woman aged 30 - 45 with an income bracket of $70k +

Industry/Entity Type

Event Planning

Contact Information for Business Card

Marnie
hello@fennwhistle.co.nz
www.fennwhistle.co.nz
02739418207

Number of Pages Required

5+ page

Requirements
Must have
• Vibrant colours and design (we love the vibrant pink and gold in the inspiration file)
• We would love to see some colour and creativity (although the black and gold is very striking). Because we are doing such minimal print work I am happy for the cards to be a little more expensive so if you want to use cut outs, rounded corners, gold foil, non standard size etc I am happy for that too. I really want the wow factor.
Nice to have
• We would like the design to be double sided.
Should not have
• The logo colour changed
• Use of Purple or Green or solid black background.
• Wedding Photos!

```html
<!DOCTYPE html>
<html lang="en">
<head>
<meta charset="utf-8">
<title>Fenn and Whistle – Business Card</title>
<link rel="stylesheet" href="https://fonts.googleapis.com/css2?family=Tinos:wght@400;700&display=swap">
<style>
  :root {
    --backdrop: #dcdcdc;
    --card-deep: #b0124f;
    --card-bright: #e23a7c;
    --gold: #e2b43a;
    --ink-light: #ffffff;
    --icon-ink: #8e0e40;
    --photo-a: #5b5f58;
    --photo-b: #b9b4a8;
    --photo-c: #e6ddcf;
  }
  * { margin: 0; padding: 0; box-sizing: border-box; }
  html, body {
    width: 1189px; height: 1200px; overflow: hidden;
    background: var(--backdrop);
  }
  .canvas { position: relative; width: 1189px; height: 1200px; }
  .card {
    position: absolute; left: 140px; width: 917px; height: 523px;
    background: linear-gradient(135deg, var(--card-bright) 0%, var(--card-deep) 100%);
    box-shadow: 0 4px 10px rgba(0,0,0,0.35);
    overflow: hidden;
    font-family: "Tinos", "Times New Roman", serif;
  }
  .card--front { top: 46px; }
  .card--back { top: 623px; }

  .photo-area {
    position: absolute; left: 0; top: 0; width: 457px; height: 523px;
    background: linear-gradient(135deg, var(--photo-a) 0%, var(--photo-b) 55%, var(--photo-c) 100%);
  }
  .gold-bar {
    position: absolute; left: 457px; top: 0; width: 14px; height: 523px;
    background: var(--gold);
  }
  .brand-ring {
    position: absolute; border: 4px solid var(--gold); border-radius: 50%;
  }
  .card--front .brand-ring { left: 597px; top: 39px; width: 168px; height: 168px; }
  .card--back .brand-ring { left: 325px; top: 74px; width: 248px; height: 248px; border-width: 5px; }

  .brand-name {
    position: absolute; text-align: center;
    color: var(--gold); font-weight: 700; white-space: nowrap;
  }
  .card--front .brand-name { left: 481px; width: 400px; top: 222px; font-size: 38px; line-height: 48px; }
  .card--back .brand-name { left: 149px; width: 600px; top: 340px; font-size: 58px; line-height: 70px; }

  .contact-name {
    position: absolute; left: 525px; top: 312px;
    color: var(--gold); font-size: 42px; line-height: 50px;
  }
  .contact-list { position: absolute; left: 522px; top: 372px; list-style: none; }
  .contact-list li {
    display: flex; align-items: center; height: 40px;
    color: var(--ink-light); font-size: 26px;
  }
  .contact-list svg { width: 20px; height: 20px; margin-right: 21px; flex: none; }
</style>
</head>
<body>
<div class="canvas">
  <section class="card card--front">
    <div class="photo-area" role="img" aria-label="Photograph of a celebration guest holding a bouquet outdoors"></div>
    <div class="gold-bar"></div>
    <div class="brand-ring"></div>
    <div class="brand-name">Fenn and Whistle</div>
    <div class="contact-name">Marnie</div>
    <ul class="contact-list">
      <li>
        <svg viewBox="0 0 20 20" aria-hidden="true"><rect width="20" height="20" fill="var(--gold)"/><path d="M6 4 L9 4 L9 7 L7.5 8 Q9 12 12 12.5 L13 11 L16 11 L16 14 Q10 17 5 10 Q4 7 6 4 Z" fill="var(--icon-ink)"/></svg>
        02739418207
      </li>
      <li>
        <svg viewBox="0 0 20 20" aria-hidden="true"><rect width="20" height="20" fill="var(--gold)"/><circle cx="10" cy="10" r="6.5" fill="none" stroke="var(--icon-ink)" stroke-width="1.6"/><path d="M3.5 10 H16.5 M10 3.5 Q6 10 10 16.5 M10 3.5 Q14 10 10 16.5" fill="none" stroke="var(--icon-ink)" stroke-width="1.2"/></svg>
        www.fennwhistle.co.nz
      </li>
      <li>
        <svg viewBox="0 0 20 20" aria-hidden="true"><rect width="20" height="20" fill="var(--gold)"/><rect x="3.5" y="5.5" width="13" height="9" fill="none" stroke="var(--icon-ink)" stroke-width="1.5"/><path d="M3.5 5.5 L10 11 L16.5 5.5" fill="none" stroke="var(--icon-ink)" stroke-width="1.5"/></svg>
        hello@fennwhistle.co.nz
      </li>
    </ul>
  </section>

  <section class="card card--back">
    <div class="brand-ring"></div>
    <div class="brand-name">Fenn and Whistle</div>
  </section>
</div>
</body>
</html>
```